Erstellung einer ersten Einladungskarte „Safe the Date“
Zielgruppe
Spezialist für temporäres Linienmanagement & Projektmanagement
Als Sozietät für professionelles Interim Management bündelt die brückwerk AG die fachliche Kompetenz und die langjährige Erfahrung erfolgreicher Führungspersönlichkeiten aus nahezu allen Sektoren der Wirtschaft. Wir unterstützen unsere Kunden bei der Bewältigung temporärer Herausforderungen im Linienmanagement sowie im Management komplexer strategischer Projekte und Programme.
https://www.brueckwerk-example.net/de/home.html
Aufgabenstellung
Siehe angehängtes Briefing und angehängtes CD Manual, das nicht zwingend eingehalten werden muss für diesen Job

```html
<!DOCTYPE html>
<html lang="de">
<head>
<meta charset="utf-8">
<title>brückwerk AG – Safe the Date</title>
<link rel="stylesheet" href="https://fonts.googleapis.com/css2?family=Fira+Sans:wght@400;500;600;700&family=Fira+Sans+Condensed:wght@600;700&display=swap">
<style>
  :root {
    --orange: #e8650f;
    --blue: #3d6a87;
    --ink: #3b5470;
    --text: #4a5866;
    --white: #ffffff;
    --frame: #2b2b2b;
    --shadow: rgba(0, 0, 0, 0.35);
  }
  * { box-sizing: border-box; margin: 0; padding: 0; }
  html, body { width: 889px; height: 1200px; overflow: hidden; background: var(--white); }
  body { position: relative; font-family: "Fira Sans", Arial, sans-serif; color: var(--text); }

  .brand-name { font-family: "Fira Sans", Arial, sans-serif; font-weight: 500; color: var(--blue); letter-spacing: 0.5px; white-space: nowrap; }
  .brand-dot { display: inline-block; border-radius: 50%; background: var(--orange); }

  .masthead { position: absolute; left: 67px; top: 120px; display: flex; align-items: center; gap: 18px; }
  .masthead .brand-dot { width: 64px; height: 64px; }
  .masthead .brand-name { font-size: 62px; }

  .card { position: absolute; left: 67px; width: 749px; height: 357px; background: var(--white); box-shadow: 5px 6px 6px var(--shadow); overflow: hidden; }
  .card svg.notch { position: absolute; left: 0; top: 0; }

  .save-card { top: 339px; border: 2px solid var(--frame); }
  .save-card .orange-field { position: absolute; left: 0; top: 0; width: 481px; height: 100%; background: var(--orange); }
  .save-card .headline { position: absolute; left: 59px; top: 196px; font-family: "Fira Sans Condensed", "Arial Narrow", sans-serif; font-weight: 700; font-size: 41px; letter-spacing: 2px; color: var(--white); }
  .save-card .brand-block { position: absolute; left: 481px; top: 0; width: 266px; height: 100%; display: flex; flex-direction: column; align-items: center; justify-content: center; gap: 26px; }
  .save-card .brand-dot { width: 62px; height: 62px; }
  .save-card .brand-name { font-size: 40px; }

  .invite-card { top: 760px; border: 1px solid #9a9a9a; }
  .invite-card .title-band { position: absolute; left: 0; top: 0; width: 481px; height: 84px; background: var(--orange); display: flex; align-items: center; justify-content: center; }
  .invite-card .title { font-family: "Fira Sans Condensed", "Arial Narrow", sans-serif; font-weight: 600; font-size: 35px; letter-spacing: 1px; color: var(--white); }
  .invite-card .header-brand { position: absolute; left: 481px; top: 0; width: 268px; height: 84px; display: flex; align-items: center; justify-content: center; }
  .invite-card .header-brand .brand-name { font-size: 34px; }
  .invite-card .blue-panel { position: absolute; left: 481px; top: 84px; width: 268px; height: 273px; background: var(--blue); display: flex; flex-direction: column; align-items: center; justify-content: center; gap: 18px; }
  .invite-card .blue-panel .brand-dot { width: 96px; height: 96px; }
  .invite-card .blue-panel .brand-name { font-size: 30px; color: var(--white); }

  .announcement { position: absolute; left: 92px; top: 98px; font-weight: 600; font-size: 19px; line-height: 1.25; color: var(--ink); }
  .details { position: absolute; left: 23px; top: 155px; width: 440px; list-style: none; }
  .detail { position: absolute; left: 0; display: flex; align-items: center; gap: 28px; font-size: 14px; line-height: 1.5; }
  .detail strong { color: var(--ink); font-weight: 600; }
  .detail.date { top: 0; }
  .detail.place { top: 52px; }
  .detail.info { top: 108px; }
  .detail-icon { flex: 0 0 42px; width: 42px; height: 42px; }
</style>
</head>
<body>

  <header class="masthead">
    <span class="brand-dot"></span>
    <span class="brand-name">brückwerk</span>
  </header>

  <section class="card save-card">
    <div class="orange-field"></div>
    <svg class="notch" width="749" height="357" aria-hidden="true">
      <polygon points="444,202 482,202 482,238" fill="var(--white)"/>
    </svg>
    <h1 class="headline">SAFE THE DATE</h1>
    <div class="brand-block">
      <span class="brand-dot"></span>
      <span class="brand-name">brückwerk</span>
    </div>
  </section>

  <section class="card invite-card">
    <div class="title-band"><h2 class="title">Orange-Blaue Nacht</h2></div>
    <div class="header-brand"><span class="brand-name">brückwerk</span></div>
    <div class="blue-panel">
      <span class="brand-dot"></span>
      <span class="brand-name">brückwerk</span>
    </div>
    <svg class="notch" width="749" height="357" aria-hidden="true">
      <polygon points="444,21 482,21 482,55" fill="var(--white)"/>
      <polygon points="481,182 513,182 481,216" fill="var(--white)"/>
    </svg>

    <p class="announcement">Die brückwerk AG wird 10 Jahre alt,<br>das werden wir feiern.</p>

    <ul class="details">
      <li class="detail date">
        <svg class="detail-icon" viewBox="0 0 42 42" aria-hidden="true">
          <circle cx="21" cy="21" r="21" fill="var(--orange)"/>
          <path d="M11 12 H31 L21 23 Z" fill="none" stroke="var(--white)" stroke-width="2" stroke-linejoin="round"/>
          <path d="M21 23 V32 M15 32 H27" stroke="var(--white)" stroke-width="2" stroke-linecap="round"/>
          <circle cx="22" cy="16" r="1.8" fill="var(--white)"/>
        </svg>
        <span>Gefeiert wird am: <strong>1. und 2. Dezember 2017</strong></span>
      </li>
      <li class="detail place">
        <svg class="detail-icon" viewBox="0 0 42 42" aria-hidden="true">
          <circle cx="21" cy="21" r="21" fill="var(--orange)"/>
          <polygon points="21,8 24.5,17 34,17 26.5,23 29.5,33 21,27 12.5,33 15.5,23 8,17 17.5,17" fill="none" stroke="var(--white)" stroke-width="1.8" stroke-linejoin="round"/>
        </svg>
        <span>Ort: <strong>München</strong></span>
      </li>
      <li class="detail info">
        <svg class="detail-icon" viewBox="0 0 42 42" aria-hidden="true">
          <circle cx="21" cy="21" r="21" fill="var(--orange)"/>
          <circle cx="21" cy="12" r="3" fill="var(--white)"/>
          <rect x="18.5" y="18" width="5" height="15" rx="1" fill="var(--white)"/>
        </svg>
        <span>Details zur Feier sowie Möglichkeiten zur Übernachtung<br>in München werden wir rechtzeitig vor der Feier mitteilen.</span>
      </li>
    </ul>
  </section>

</body>
</html>
```